3 pages of UI design for AdTech Startup

We need 3 pages of UI design for a new AdTech company located in Seattle called KESTREL Systems.

We put digital, mobile billboards on college campuses throughout the country. This design project involves our back-end customer dashboard.

Page 1- Dashboard home page
page 2- Manage ads screen (see File 3 below for the screenshot of our current design). Please match the design of all 3 screens so there is consistency
page 3-Detailed Zone screen (see file 16 below). This page looks similar to the first page but gives a more detailed overview and a larger map.

The features and functionality are already built but we are lacking an aesthetically pleasing and slick design. Looking for someone who can match our website look to this new dashboard space. Our company reflects modern, clean, elegant design that is straight-forward and user friendly (main inspiration is VOLTA, we love their design and feel).

Target Market(s)

-Local business owner, marketing directors, and national advertising and marketing agencies

Industry/Entity Type

Advertising

Number of Pages Required

3 page

Font styles to use
Other font styles liked:
• Proxima Nova- Thin for body text, Light for title

Colors
85cae6
33a6d7
0292cd
ffffff

Requirements
Nice to have
• Please include enough detail so that my developer can look at the design you come up with and translate it to html. Please include spacing, fonts, color numbers. My developer is going to look at your creation and recreate it in html format

```html
<!DOCTYPE html>
<html lang="en">
<head>
<meta charset="utf-8">
<title>KESTREL Systems — Dashboard</title>
<link href="https://fonts.googleapis.com/css2?family=Lato:wght@300;400;700&display=swap" rel="stylesheet">
<style>
:root{
  --sky:#85cae6;
  --blue:#33a6d7;
  --deep:#0292cd;
  --white:#ffffff;
  --canvas:#eceff3;
  --row:#f3f5f8;
  --line:#e3e6ea;
  --ink:#2f3337;
  --muted:#6f757b;
  --axis:#a4a9ae;
  --bar-blue:#5b9cf0;
  --bar-pink:#f7618d;
  --bar-cyan:#2fd3e3;
  --dark-btn:#505457;
}
*{margin:0;padding:0;box-sizing:border-box}
html,body{width:1200px;height:824px;overflow:hidden}
body{font-family:"Lato",sans-serif;background:var(--canvas);color:var(--ink);position:relative}
.abs{position:absolute}

/* header */
.topbar{left:0;top:0;width:928px;height:56px;background:var(--white);border-bottom:1px solid var(--line)}
.brand{left:12px;top:14px;font-size:26px;font-weight:700;letter-spacing:.5px;color:var(--blue);display:flex;align-items:center;gap:8px}
.brand .mark{width:26px;height:26px;border:3px solid var(--blue);border-radius:4px}
.client{left:640px;top:0;width:288px;height:56px;border-left:1px solid var(--line)}
.client-name{left:16px;top:17px;font-size:20px;font-weight:700;color:var(--deep);letter-spacing:1px}
.login{left:212px;top:18px;width:60px;height:20px;background:var(--blue);color:var(--white);font-size:9px;font-weight:700;display:flex;align-items:center;justify-content:center;gap:3px;border-radius:2px}

/* sidebar */
.sidebar{left:928px;top:0;width:272px;height:824px;background:var(--canvas);border-left:1px solid var(--line)}
.help{left:0;top:0;width:272px;height:56px;background:var(--white);border-bottom:1px solid var(--line);display:flex;align-items:center;padding-left:12px;font-size:17px;gap:6px}
.help .caret{position:absolute;right:16px;top:26px;border:4px solid transparent;border-top:5px solid var(--muted)}
.stats{left:0;top:56px;width:272px;height:360px;background:var(--white)}
.stat{display:flex;align-items:center;height:46px;border-bottom:1px solid var(--line);font-size:13px}
.stat:nth-child(odd){background:var(--row)}
.stat .k{width:104px;padding-left:12px;color:var(--muted)}
.stat .c{width:16px;color:var(--muted)}
.stat .v{font-weight:700;color:var(--ink)}
.perf-head{left:0;top:416px;width:272px;height:48px;background:var(--white);border-bottom:1px solid var(--line);padding-left:17px;display:flex;align-items:center;font-size:17px}
.perf{left:0;top:464px;width:272px;height:360px;background:var(--white)}
.btn{display:flex;align-items:center;justify-content:center;color:var(--white);font-size:11px;font-weight:700}
.btn-dark{left:12px;top:149px;width:96px;height:27px;background:var(--dark-btn);font-size:10px}
.btn-blue{background:var(--blue)}
.details{left:86px;top:226px;width:108px;height:32px}

/* toolbar */
.range{left:522px;top:70px;width:156px;height:26px;background:var(--white);font-size:10px;color:var(--muted);display:flex;align-items:center;gap:6px;padding-left:10px}
.tabs{left:692px;top:70px;width:202px;height:26px;background:var(--white);display:flex;font-size:10px;color:var(--muted)}
.tab{flex:1;display:flex;align-items:center;justify-content:center}
.tab.active{background:var(--blue);color:var(--white);font-weight:700}

/* chart */
.chart{left:27px;top:110px;width:871px;height:272px;background:var(--white);border-radius:3px}

/* panels */
.panel-head{top:418px;height:46px;background:var(--white);display:flex;align-items:center;font-size:14px;border-right:1px solid var(--line)}
.card{background:var(--white)}
.zone-title{position:absolute;left:0;right:0;top:92px;text-align:center;font-size:15px;text-decoration:underline}
.zone-sub{position:absolute;left:0;right:0;top:116px;text-align:center;font-size:10px;color:var(--muted)}
.ad-photo{left:8px;top:8px;width:171px;height:166px;background:linear-gradient(160deg,#8a6a4a,#4b4a48 55%,#7f7c77)}
.msg{left:39px;top:214px;width:108px;height:32px}
.map{left:333px;top:472px;width:589px;height:270px;background:radial-gradient(ellipse at 55% 50%,#3a4552,#2b3a2a 60%,#1f2a22)}

.footer{left:0;top:776px;width:928px;height:48px;background:var(--blue);color:var(--white);font-size:11px;display:flex;align-items:center;padding-left:16px}
</style>
</head>
<body>

<header class="topbar abs">
  <div class="brand abs"><span class="mark"></span>KESTREL</div>
  <div class="client abs">
    <div class="client-name abs">PIVOT</div>
    <div class="login abs">LOGIN
      <svg width="7" height="7" viewBox="0 0 8 8"><path d="M0 3h4V1l4 3-4 3V5H0z" fill="#fff"/></svg>
    </div>
  </div>
</header>

<div class="range abs">
  <svg width="9" height="9" viewBox="0 0 10 10"><rect x=".5" y="1.5" width="9" height="8" fill="none" stroke="#9aa0a6"/><path d="M.5 4h9" stroke="#9aa0a6"/></svg>
  29/07/2016 - 05/08/2016
</div>
<nav class="tabs abs">
  <div class="tab">Hourly</div><div class="tab active">Day</div><div class="tab">Week</div><div class="tab">Month</div>
</nav>

<section class="chart abs">
  <svg width="871" height="272" viewBox="0 0 871 272" font-family="Lato, sans-serif" font-size="9" fill="#a4a9ae">
    <g stroke="#e3e6ea" stroke-dasharray="2 2">
      <path d="M59 34H827M59 59H827M59 84H827M59 109H827M59 134H827M59 159H827M59 184H827M59 209H827M59 234H827"/>
    </g>
    <g text-anchor="end">
      <text x="52" y="37">10</text><text x="52" y="62">8.75</text><text x="52" y="87">7.5</text>
      <text x="52" y="112">6.25</text><text x="52" y="137">5</text><text x="52" y="162">3.75</text>
      <text x="52" y="187">2.5</text><text x="52" y="212">1.25</text><text x="52" y="237">0</text>
    </g>
    <g text-anchor="middle">
      <text x="91" y="340" dy="-93">Jan</text><text x="155" y="247">Feb</text><text x="219" y="247">Mar</text>
      <text x="283" y="247">Apr</text><text x="347" y="247">Mai</text><text x="411" y="247">Jun</text>
      <text x="474" y="247">Jul</text><text x="538" y="247">Aug</text><text x="602" y="247">Sep</text>
      <text x="666" y="247">Oct</text><text x="730" y="247">Nov</text><text x="794" y="247">Dec</text>
    </g>
    <g fill="#5b9cf0">
      <rect x="80" y="134" width="7" height="100"/><rect x="144" y="154" width="7" height="80"/>
      <rect x="208" y="174" width="7" height="60"/><rect x="272" y="94" width="7" height="140"/>
      <rect x="336" y="134" width="7" height="100"/><rect x="400" y="34" width="7" height="200"/>
      <rect x="463" y="174" width="7" height="60"/><rect x="527" y="154" width="7" height="80"/>
      <rect x="591" y="74" width="7" height="160"/><rect x="655" y="34" width="7" height="200"/>
      <rect x="719" y="114" width="7" height="120"/><rect x="783" y="74" width="7" height="160"/>
    </g>
    <g fill="#f7618d">
      <rect x="88" y="174" width="7" height="60"/><rect x="152" y="194" width="7" height="40"/>
      <rect x="216" y="59" width="7" height="175"/><rect x="280" y="134" width="7" height="100"/>
      <rect x="344" y="154" width="7" height="80"/><rect x="408" y="114" width="7" height="120"/>
      <rect x="471" y="154" width="7" height="80"/><rect x="535" y="114" width="7" height="120"/>
      <rect x="599" y="94" width="7" height="140"/><rect x="663" y="74" width="7" height="160"/>
      <rect x="727" y="94" width="7" height="140"/><rect x="791" y="154" width="7" height="80"/>
    </g>
    <g fill="#2fd3e3">
      <rect x="96" y="114" width="7" height="120"/><rect x="160" y="174" width="7" height="60"/>
      <rect x="224" y="134" width="7" height="100"/><rect x="288" y="59" width="7" height="175"/>
      <rect x="352" y="74" width="7" height="160"/><rect x="416" y="134" width="7" height="100"/>
      <rect x="479" y="114" width="7" height="120"/><rect x="543" y="74" width="7" height="160"/>
      <rect x="607" y="174" width="7" height="60"/><rect x="671" y="194" width="7" height="40"/>
      <rect x="735" y="174" width="7" height="60"/><rect x="799" y="114" width="7" height="120"/>
    </g>
  </svg>
</section>

<div class="panel-head abs" style="left:0;width:136px;padding-left:18px">Zoone</div>
<div class="panel-head abs" style="left:136px;width:191px;padding-left:14px">Active Ad</div>
<div class="panel-head abs" style="left:327px;width:601px;padding-left:15px;border-right:0">Career Paths</div>

<section class="card abs" style="left:3px;top:468px;width:133px;height:278px">
  <div class="zone-title">Zoone 1</div>
  <div class="zone-sub">Elm Street House</div>
</section>

<section class="card abs" style="left:139px;top:468px;width:186px;height:278px">
  <div class="ad-photo abs" role="img" aria-label="Photo of students walking on campus wearing backpacks with digital billboard screens"></div>
  <div class="msg btn btn-blue abs">Messages</div>
</section>

<section class="card abs" style="left:329px;top:468px;width:597px;height:278px"></section>
<div class="map abs" role="img" aria-label="Satellite map of the Seattle area with the tracked career path route outlined"></div>

<footer class="footer abs">2016 © Kestrel Systems.</footer>

<aside class="sidebar abs">
  <div class="help abs">
    <svg width="15" height="15" viewBox="0 0 16 16"><circle cx="8" cy="8" r="7" fill="none" stroke="#2f3337" stroke-width="1.2"/><path d="M6 6.2a2 2 0 1 1 2.6 1.9c-.5.2-.6.5-.6 1v.6" fill="none" stroke="#2f3337" stroke-width="1.2"/><circle cx="8" cy="11.6" r=".8" fill="#2f3337"/></svg>
    HELP<span class="caret"></span>
  </div>
  <div class="stats abs">
    <div class="stat"><span class="k">Rotatins</span><span class="c">:</span><span class="v">85</span></div>
    <div class="stat"><span class="k">TIme</span><span class="c">:</span><span class="v">21:25 Min</span></div>
    <div class="stat"><span class="k">Impressions</span><span class="c">:</span><span class="v">595</span></div>
    <div class="stat"><span class="k">Miles</span><span class="c">:</span><span class="v">0.3 Miles</span></div>
  </div>
  <div class="perf-head abs">Zone Performance</div>
  <div class="perf abs">
    <div class="stat"><span class="k">Rotatins</span><span class="c">:</span><span class="v">85</span></div>
    <div class="stat"><span class="k">Broadcast Time</span><span class="c">:</span><span class="v">21:25 Min</span></div>
    <div class="stat"><span class="k">Miles Walked</span><span class="c">:</span><span class="v">595</span></div>
    <div class="btn btn-dark abs">Text Messages</div>
    <div class="details btn btn-blue abs">Details</div>
  </div>
</aside>

</body>
</html>
```